Website for company called VELQUOgen

We need a website for our new company called VELQUOgen which developed a platform/technology to identify antigen-specific T cells (immune cells) which can be used for cancer therapy, autoimmunity, etc.

The platform is called VELQUO and is rapid, versatile, unbiased, and inexpensive.

We have a semi-final logo although we are not completely set on color and font of text (attached).

Target Market(s)

Our target audience at the moment would be potential investors and VCs. We eventually are interested in getting attention from scientists and cell/immunotherapy companies.

Industry/Entity Type

Healthcare/Technology

Coding

Coded - Design and coding required

Number of Pages Required

1 page

Colors
0094D4
00A9DD
6FCCEA
C7EBF8
E9F6FB
00AB8E
00BBA5
67D7C9
C6EFE9
E9F9F6
E54698
E96AAD
F1A4CE
F9D9EA
FCEFF6
A7469A
B969AE
D3A5CF
EDDBEB
F8F0F9
6B429C
8869AF
B7A5CE
E3DAEB
F3F0F8

Requirements
Must have
• Landing page about the company, About us page, Technology page (could be merged with company landing page), Contact us page

```html
<!DOCTYPE html>
<html lang="en">
<head>
<meta charset="utf-8">
<title>VELQUOgen</title>
<link href="https://fonts.googleapis.com/css2?family=Archivo:wght@500;600;700;800&family=Urbanist:wght@400;500;600;700&display=swap" rel="stylesheet">
<style>
:root{
  --ink:#111318;
  --body:#3a3d48;
  --violet:#5b47a8;
  --violet-soft:#8869AF;
  --blue:#0f72d8;
  --sky:#6FCCEA;
  --pale:#EEF3FA;
  --white:#ffffff;
  --field-text:#3b3f4a;
  --heading:"Archivo",sans-serif;
  --text:"Urbanist",sans-serif;
}
*{box-sizing:border-box;margin:0;padding:0}
html,body{width:1200px;height:2930px;overflow:hidden;background:var(--white)}
body{position:relative;font-family:var(--text);color:var(--body)}
.abs{position:absolute}

/* header */
.site-header{position:absolute;left:0;top:0;width:1200px;height:82px;background:var(--white)}
.brand{position:absolute;display:flex;align-items:center;gap:8px;font-family:var(--text);font-weight:700;color:var(--ink)}
.brand-dot{width:14px;height:14px;border-radius:50%;background:var(--ink)}
.site-header .brand{left:139px;top:22px;font-size:34px}
.main-nav a{position:absolute;top:39px;font-size:15px;font-weight:600;color:var(--ink);text-decoration:none;letter-spacing:.2px}
.main-nav .active{color:var(--violet)}
.main-nav .active::after{content:"";position:absolute;left:-2px;right:-2px;top:26px;height:3px;background:var(--blue);border-radius:2px}
.btn{position:absolute;display:flex;align-items:center;justify-content:center;gap:8px;font-family:var(--text);font-weight:700;text-decoration:none;border-radius:30px}
.btn-header{left:912px;top:26px;width:146px;height:39px;background:var(--violet);color:var(--white);font-size:13px}

/* hero */
.hero-visual{position:absolute;left:0;top:82px;width:1200px;height:652px;background:
 radial-gradient(circle at 870px 300px,#3b3fa8 0,#4a56c2 120px,transparent 260px),
 radial-gradient(circle at 1050px 520px,#d7b7dc 0,transparent 180px),
 linear-gradient(100deg,#5b4fb4 0%,#6b6bc6 40%,#4f8fc9 75%,#65b7d8 100%)}
.hero-band{position:absolute;left:0;top:732px;width:1200px;height:4px;background:var(--sky)}
.eyebrow{font-size:15px;font-weight:700;letter-spacing:3.5px}
.hero .eyebrow{position:absolute;left:123px;top:243px;color:var(--white)}
.hero h1{position:absolute;left:118px;top:276px;font-family:var(--heading);font-weight:800;font-size:58px;line-height:60px;color:var(--white);text-transform:uppercase;letter-spacing:-.5px}
.hero h1 .light{font-weight:500}
.btn-outline{left:118px;top:478px;width:197px;height:52px;border:2px solid var(--white);color:var(--white);font-size:15px}

/* about */
.about-frame{position:absolute;background:linear-gradient(160deg,#6FCCEA,#C7EBF8)}
.photo{position:absolute}
.about .eyebrow{position:absolute;left:624px;top:863px;color:var(--blue)}
.section-title{font-family:var(--heading);font-weight:700;color:var(--ink);letter-spacing:-.5px}
.about h2{position:absolute;left:624px;top:884px;font-size:52px}
.title-rule{position:absolute;height:2px;background:var(--violet-soft)}
.title-rule::before{content:"";position:absolute;left:0;top:-1px;width:38px;height:4px;background:var(--violet)}
.mark-circle{position:absolute;width:22px;height:22px;border-radius:50%;background:var(--blue)}
.about-copy{position:absolute;left:630px;top:976px;width:492px;font-size:18px;line-height:26px;color:var(--body)}
.about-copy p+p{margin-top:26px}
.btn-fill{left:628px;top:1209px;width:161px;height:43px;background:var(--violet);color:var(--white);font-size:14px}

/* technology */
.tech{position:absolute;left:0;top:1378px;width:1200px;height:657px;background:var(--pale);overflow:hidden}
.tech .eyebrow{position:absolute;left:138px;top:108px;color:var(--blue)}
.tech h2{position:absolute;left:138px;top:126px;font-size:50px}
.tech-intro{position:absolute;left:138px;top:210px;width:400px;font-size:18px;line-height:26px}
.tech-points{position:absolute;left:143px;top:320px;list-style:none;width:400px}
.tech-points li{position:relative;padding-left:22px;font-size:18px;line-height:26px;font-weight:700;color:var(--ink);margin-bottom:32px}
.tech-points li::before{content:"";position:absolute;left:0;top:9px;width:8px;height:8px;background:var(--blue)}

/* contact */
.contact{position:absolute;left:0;top:2035px;width:1200px;height:599px;background:
 radial-gradient(circle at 200px 420px,#4d9be3 0,transparent 260px),
 radial-gradient(circle at 1000px 150px,#5aa6e8 0,transparent 280px),
 linear-gradient(180deg,#2e7fd8,#3a8fe0)}
.contact .mark-circle{left:589px;top:50px;background:var(--white)}
.contact .eyebrow{position:absolute;left:0;width:1200px;top:97px;text-align:center;color:var(--white)}
.contact h2{position:absolute;left:0;width:1200px;top:111px;text-align:center;font-family:var(--heading);font-weight:700;font-size:46px;color:var(--white)}
.contact .underline{position:absolute;left:580px;top:172px;width:58px;height:2px;background:var(--white)}
.field{position:absolute;background:var(--white);display:flex;align-items:center;gap:10px;padding-left:24px;font-size:15px;font-weight:500;color:var(--field-text)}
.field svg{flex:none}
.field-area{align-items:flex-start;padding-top:20px}
.btn-send{left:518px;top:487px;width:191px;height:44px;border:2px solid var(--white);color:var(--white);font-size:16px}

/* footer */
.site-footer .brand{left:156px;top:2700px;font-size:38px}
.socials{position:absolute;left:156px;top:2769px;display:flex;gap:8px}
.socials span{width:34px;height:34px;border-radius:50%;background:var(--violet)}
.copyright{position:absolute;left:156px;top:2823px;font-size:13px;color:var(--ink)}
.foot-col{position:absolute;top:2696px}
.foot-col h3{font-family:var(--text);font-size:18px;font-weight:700;color:var(--ink);border-left:3px solid var(--blue);padding-left:8px;line-height:20px}
.foot-col ul{list-style:none;margin-top:18px;padding-left:11px}
.foot-col li{font-size:15px;line-height:26px;color:var(--ink)}
.contact-line{display:flex;align-items:center;gap:12px;margin-top:16px;font-size:13px;line-height:17px;color:var(--ink)}
.contact-line .ic{width:36px;height:36px;border-radius:50%;background:var(--violet);display:flex;align-items:center;justify-content:center}
</style>
</head>
<body>

<header class="site-header">
  <div class="brand"><span class="brand-dot"></span>VELQUOgen</div>
  <nav class="main-nav">
    <a class="active" style="left:520px">HOME</a>
    <a style="left:624px">ABOUT US</a>
    <a style="left:757px">TECHNOLOGY</a>
  </nav>
  <a class="btn btn-header">CONTACT US <span>›</span></a>
</header>

<section class="hero">
  <div class="hero-visual" role="img" aria-label="Blue DNA double helix with an immune cell on a violet and teal background"></div>
  <div class="hero-band"></div>
  <div class="eyebrow">WELCOME TO VELQUOGEN</div>
  <h1><span class="light">Unlocking the</span><br>Power of the<br>Immune System</h1>
  <a class="btn btn-outline">LEARN MORE <span>›</span></a>
</section>

<section class="about">
  <div class="about-frame" style="left:83px;top:857px;width:112px;height:80px"></div>
  <div class="about-frame" style="left:455px;top:1180px;width:108px;height:83px"></div>
  <div class="photo" role="img" aria-label="Scientist looking through a microscope in a lab" style="left:98px;top:871px;width:223px;height:320px;background:linear-gradient(160deg,#dfe6ee,#b9c6d6 60%,#8aa4c4)"></div>
  <div class="photo" role="img" aria-label="Red cell clusters inside a clear membrane over a DNA strand" style="left:330px;top:933px;width:223px;height:320px;background:radial-gradient(circle at 110px 160px,#e8745e 0,#c9564c 50px,transparent 90px),linear-gradient(160deg,#3d5a98,#6d88c4 50%,#3b5593)"></div>
  <div class="abs" style="left:297px;top:1052px;width:63px;height:63px;border-radius:50%;background:var(--white)"></div>
  <div class="mark-circle" style="left:318px;top:1073px"></div>

  <div class="eyebrow">WHO WE ARE</div>
  <h2 class="section-title">About VELQUOgen</h2>
  <div class="title-rule" style="left:627px;top:953px;width:166px"></div>
  <div class="about-copy">
    <p>Lorem ipsum dolor sit amet, consectetur adipiscing elit, sed do eiusmod tempor incididunt ut labore et dolore magna aliqua. Ut enim ad minim veniam, quis nostrud exercitation ullamco laboris nisi ut aliquip ex ea commodo consequat.</p>
    <p>Duis aute irure dolor in reprehenderit in voluptate velit esse cillum dolore eu fugiat nulla pariatur. Excepteur sint occaecat cupidatat non proident, sunt in culpa qui officia</p>
  </div>
  <a class="btn btn-fill">LEARN MORE <span>›</span></a>
</section>

<section class="tech">
  <svg class="abs" style="left:0;top:0" width="1200" height="657" viewBox="0 0 1200 657">
    <defs>
      <radialGradient id="cellTone" cx="0.7" cy="0.4" r="0.7">
        <stop offset="0" stop-color="#2bb3b8"/>
        <stop offset="0.45" stop-color="#1b8fa6"/>
        <stop offset="1" stop-color="#0f5f7e"/>
      </radialGradient>
    </defs>
    <circle cx="1320" cy="322" r="716" fill="none" stroke="var(--blue)" stroke-width="8"/>
    <circle cx="1320" cy="322" r="708" fill="url(#cellTone)" role="img" aria-label="Teal T cell floating among smaller cells"/>
  </svg>
  <div class="eyebrow">WHY WE ARE</div>
  <h2 class="section-title">Technology</h2>
  <div class="title-rule" style="left:140px;top:190px;width:170px"></div>
  <p class="tech-intro">Lorem ipsum dolor sit amet, consectetur adipiscing elit, sed do eiusmod tempor incididunt ut labore et dolore magna aliqua.</p>
  <ul class="tech-points">
    <li>Lorem ipsum dolor sit amet, consectetur adipiscing elit, sed do eiusmod</li>
    <li>Lorem ipsum dolor sit amet, consectetur adipiscing elit, sed do eiusmod</li>
    <li>Lorem ipsum dolor sit amet, consectetur adipiscing elit, sed do eiusmod</li>
  </ul>
</section>

<section class="contact">
  <div class="mark-circle"></div>
  <div class="eyebrow">CONTACT US</div>
  <h2>Leave us a Message</h2>
  <div class="underline"></div>

  <div class="field" style="left:243px;top:208px;width:362px;height:53px">
    <svg width="14" height="14" viewBox="0 0 14 14"><circle cx="7" cy="4" r="3.2" fill="#8a93b0"/><path d="M1 14c0-4 3-6 6-6s6 2 6 6z" fill="#8a93b0"/></svg>First Name</div>
  <div class="field" style="left:619px;top:208px;width:361px;height:53px">
    <svg width="14" height="14" viewBox="0 0 14 14"><circle cx="7" cy="4" r="3.2" fill="#8a93b0"/><path d="M1 14c0-4 3-6 6-6s6 2 6 6z" fill="#8a93b0"/></svg>Last Name</div>
  <div class="field" style="left:243px;top:276px;width:362px;height:53px">
    <svg width="16" height="12" viewBox="0 0 16 12"><rect width="16" height="12" rx="1.5" fill="#8a93b0"/><path d="M1 1l7 6 7-6" fill="none" stroke="#fff" stroke-width="1.3"/></svg>Email address</div>
  <div class="field" style="left:619px;top:276px;width:361px;height:53px">
    <svg width="14" height="14" viewBox="0 0 14 14"><path d="M3 1l2 3-1.3 1.5c.8 1.8 2.2 3.2 4 4L9.2 8l3 2-1 2.5C6 12 2 8 1.5 2.8z" fill="#8a93b0"/></svg>Phone</div>
  <div class="field field-area" style="left:243px;top:343px;width:737px;height:121px">
    <svg width="15" height="13" viewBox="0 0 15 13"><ellipse cx="7.5" cy="5.5" rx="7" ry="5" fill="#8a93b0"/><path d="M3 9l-1 4 4-2.5z" fill="#8a93b0"/></svg>Leave Message</div>
  <a class="btn btn-send">Send Message <span>›</span></a>
</section>

<footer class="site-footer">
  <div class="brand"><span class="brand-dot"></span>VELQUOgen</div>
  <div class="socials"><span></span><span></span><span></span></div>
  <p class="copyright">© 2025 VELQUOgen. All Rights Reserved</p>

  <div class="foot-col" style="left:514px">
    <h3>Navigation</h3>
    <ul><li>Home</li><li>About</li><li>Technology</li><li>Contact</li></ul>
  </div>
  <div class="foot-col" style="left:713px">
    <h3>Resources</h3>
    <ul style="padding-left:12px"><li>Sitemap</li><li>Terms of Use</li><li>Terms of Use</li></ul>
  </div>
  <div class="foot-col" style="left:884px">
    <h3>Contact Us</h3>
    <div class="contact-line" style="margin-top:22px;padding-left:11px">
      <span class="ic"><svg width="16" height="16" viewBox="0 0 14 14"><path d="M3 1l2 3-1.3 1.5c.8 1.8 2.2 3.2 4 4L9.2 8l3 2-1 2.5C6 12 2 8 1.5 2.8z" fill="#fff"/></svg></span>
      <span>Phone Number<br>(555) 014-2290</span>
    </div>
    <div class="contact-line" style="padding-left:11px">
      <span class="ic"><svg width="16" height="12" viewBox="0 0 16 12"><rect width="16" height="12" rx="1.5" fill="#fff"/><path d="M1 1l7 6 7-6" fill="none" stroke="#5b47a8" stroke-width="1.3"/></svg></span>
      <span>hello@velquogen.example</span>
    </div>
  </div>
</footer>

</body>
</html>
```